Get Up to $ 500,000 in Business Capital within 48 hours

design a flyer offering business capital to businesses. The flyer is going to be mailed to business owners and the flyer needs to immediately capture their attention.
The flyer needs to be bold and professional and really stand-out.
pppppppppppppppppppppppppppppppppppppppppppppppppppppppppppppppppppppppppppppppppppppppppppppppppppppppppppppppppppppppppppppppppppppppppppppppppppppppppppppppppppppppppppppppppppppppppppppppppppppppppppppppppppppppppppppppppppppp

Target Market(s)

business owners

Font styles to use
Serif

Requirements
Must have
• Apply online in minutes at PellarCapital.example or call 800-GRAB-NOW
Nice to have
• We fund almost every business type. Not a business loan, receive a cash advance on your future sales.

```html
<!DOCTYPE html>
<html lang="en">
<head>
<meta charset="utf-8">
<title>Pellar Capital – Business Capital Flyer</title>
<link rel="stylesheet" href="https://fonts.googleapis.com/css2?family=Montserrat:wght@500;600;700;800;900&display=swap">
<style>
  :root {
    --page-bg: #3a3637;
    --brand-blue: #2a73c4;
    --headline-blue: #1d5fc4;
    --band-blue: #1f4fb2;
    --band-light: #2b8ad6;
    --navy: #1d3a9a;
    --ink: #17213a;
    --paper: #f4f1f6;
    --white: #ffffff;
  }
  * { box-sizing: border-box; margin: 0; padding: 0; }
  html, body { width: 1200px; height: 800px; overflow: hidden; }
  body {
    background: var(--page-bg);
    font-family: "Montserrat", Arial, sans-serif;
    position: relative;
  }
  .flyer {
    position: absolute;
    left: 324px; top: 10px;
    width: 552px; height: 780px;
    background: var(--paper);
    overflow: hidden;
    box-shadow: 0 6px 24px rgba(0,0,0,.35);
  }
  .hero-photo {
    position: absolute; left: 0; top: 0; width: 552px; height: 300px;
    background:
      linear-gradient(180deg, rgba(0,0,0,0) 70%, rgba(110,85,60,.55) 100%),
      linear-gradient(90deg, #f3e9f1 0%, #ead9e7 28%, #c9c98f 52%, #8fb258 72%, #6f9c45 100%);
  }
  .brand {
    position: absolute; left: 32px; top: 42px;
    font-size: 24px; font-weight: 600; letter-spacing: .5px;
    color: var(--brand-blue);
  }
  .headline {
    position: absolute; left: 32px; top: 86px;
    font-size: 40px; line-height: 1.04; font-weight: 900;
    color: var(--headline-blue); text-transform: uppercase;
  }
  .offer-band {
    position: absolute; left: 0; top: 300px; width: 552px; height: 80px;
  }
  .offer-band svg { position: absolute; inset: 0; }
  .offer-text {
    position: absolute; left: 28px; top: 313px; width: 420px;
    font-size: 22px; line-height: 1.2; font-weight: 800; color: var(--white);
  }
  .hands-photo {
    position: absolute; left: 312px; top: 380px; width: 240px; height: 340px;
    background: linear-gradient(160deg, #dfe9e3 0%, #cfdcd6 40%, #e6cfc4 70%, #efe7ec 100%);
  }
  .feature {
    position: absolute; display: flex; align-items: center; gap: 12px;
    font-size: 14px; font-weight: 700; color: var(--ink); line-height: 1.2;
  }
  .feature svg { flex: 0 0 auto; }
  .feature--credit { left: 28px; top: 398px; width: 260px; }
  .feature--application { left: 28px; top: 472px; width: 260px; }
  .checklist {
    position: absolute; left: 28px; top: 556px; width: 272px; list-style: none;
  }
  .checklist li {
    display: flex; gap: 10px; align-items: flex-start;
    font-size: 13.5px; font-weight: 700; color: var(--ink); line-height: 1.25;
    margin-bottom: 12px;
  }
  .checklist li:last-child { margin-bottom: 0; }
  .checklist svg { flex: 0 0 auto; margin-top: 1px; }
  .cta-bar {
    position: absolute; left: 0; top: 720px; width: 552px; height: 60px;
    padding: 0 12px;
    background: var(--navy); color: var(--white);
    display: flex; align-items: center; justify-content: center;
    font-size: 11.5px; font-weight: 500; white-space: nowrap;
  }
  .cta-bar strong { font-weight: 800; }
</style>
</head>
<body>
  <article class="flyer">
    <div class="hero-photo" role="img" aria-label="Stacks of coins in soil with seedlings growing taller from each stack"></div>
    <div class="brand">PELLAR CAPITAL</div>
    <h1 class="headline">Need Business<br>Capital?</h1>

    <div class="offer-band">
      <svg width="552" height="80" viewBox="0 0 552 80" aria-hidden="true">
        <rect x="0" y="0" width="552" height="80" fill="var(--band-blue)"/>
        <polygon points="430,0 552,0 552,80 470,80" fill="var(--band-light)"/>
      </svg>
    </div>
    <p class="offer-text">You can qualify for up to 500,000<br>in just 24 hours.</p>

    <div class="hands-photo" role="img" aria-label="Adult hands passing a jar of coins with a seedling to a child's open hands"></div>

    <div class="feature feature--credit">
      <svg width="60" height="60" viewBox="0 0 60 60" aria-hidden="true">
        <circle cx="30" cy="30" r="28" fill="var(--band-blue)"/>
        <circle cx="30" cy="30" r="23" fill="none" stroke="#fff" stroke-width="2"/>
        <circle cx="28" cy="24" r="7" fill="none" stroke="#fff" stroke-width="2"/>
        <text x="28" y="28" font-size="10" font-weight="700" fill="#fff" text-anchor="middle" font-family="Montserrat, sans-serif">$</text>
        <path d="M17 40 h8 l6 3 h10 l4-4" fill="none" stroke="#fff" stroke-width="2" stroke-linecap="round" stroke-linejoin="round"/>
      </svg>
      <span>No minimum<br>credit score</span>
    </div>

    <div class="feature feature--application">
      <svg width="60" height="60" viewBox="0 0 60 60" aria-hidden="true">
        <circle cx="30" cy="30" r="28" fill="var(--band-blue)"/>
        <circle cx="30" cy="30" r="23" fill="none" stroke="#fff" stroke-width="2"/>
        <rect x="20" y="17" width="20" height="26" rx="2" fill="none" stroke="#fff" stroke-width="2"/>
        <path d="M24 24 h12 M24 30 h12 M24 36 h8" stroke="#fff" stroke-width="2" stroke-linecap="round"/>
      </svg>
      <span>Simple 1 page<br>application</span>
    </div>

    <ul class="checklist">
      <li>
        <svg width="18" height="18" viewBox="0 0 18 18" aria-hidden="true"><circle cx="9" cy="9" r="8" fill="none" stroke="var(--band-blue)" stroke-width="2"/><path d="M5 9 l3 3 l6-7" fill="none" stroke="var(--band-blue)" stroke-width="2.4" stroke-linecap="round"/></svg>
        <span>Not a business loan, get a cash advance today on your future sales.</span>
      </li>
      <li>
        <svg width="18" height="18" viewBox="0 0 18 18" aria-hidden="true"><circle cx="9" cy="9" r="8" fill="none" stroke="var(--band-blue)" stroke-width="2"/><path d="M5 9 l3 3 l6-7" fill="none" stroke="var(--band-blue)" stroke-width="2.4" stroke-linecap="round"/></svg>
        <span>Convenient alternative to<br>a bank loan.</span>
      </li>
      <li>
        <svg width="18" height="18" viewBox="0 0 18 18" aria-hidden="true"><circle cx="9" cy="9" r="8" fill="none" stroke="var(--band-blue)" stroke-width="2"/><path d="M5 9 l3 3 l6-7" fill="none" stroke="var(--band-blue)" stroke-width="2.4" stroke-linecap="round"/></svg>
        <span>We fund virtually every<br>type of business.</span>
      </li>
    </ul>

    <footer class="cta-bar">
      <span><strong>Apply in minutes online at</strong> PellarCapital.example <strong>or call</strong> 1-800-GRAB-NOW</span>
    </footer>
  </article>
</body>
</html>
```